Platelet Rich Plasma (PRP) Flyer

Hi,

Looking to spruce up our Platelet Rich Plasma Flyer (see power point attachment). I also included previous flyers as examples on the design style we are looking for.

Quorum is our official font of our logo.
Attached is our logo in EPS format.
Please use the current photos in the power point. If you include photos, please make sure the stock image is free.

Files must be under 5MB. JPEG, PNG, PDF, .ai

Thank you,
Dorian

Target Market(s)

Patients

Industry/Entity Type

Healthcare

Font styles to use
Other font styles liked:
• Quorum

Requirements
Must have
• Emphasis on Platelet Rich Plasma Therapy when they pick up the flyer. The price of $199. FSA/HSA Eligible. The different treatment areas. The three addresses. Best of the best logo can be very small, not as important.
Nice to have
• One or two pictures. Less is more
Should not have
• Long paragraphs, multiple sentences.

```html
<!DOCTYPE html>
<html lang="en">
<head>
<meta charset="utf-8">
<title>Platelet Rich Plasma Therapy Flyer</title>
<link href="https://fonts.googleapis.com/css2?family=Dancing+Script:wght@700&family=Montserrat:wght@700;800&family=Outfit:wght@300;400;500;600;700&display=swap" rel="stylesheet">
<style>
  :root{
    --ink:#2e2e2e;
    --teal:#47bf9f;
    --orange:#ee7b43;
    --white:#ffffff;
    --dark-text:#2a2a2a;
  }
  *{margin:0;padding:0;box-sizing:border-box}
  html,body{width:934px;height:1200px;overflow:hidden;background:var(--white)}
  .flyer{position:relative;width:934px;height:1200px;background:var(--ink);overflow:hidden;font-family:"Outfit",sans-serif;color:var(--white)}
  .hero-art{position:absolute;left:0;top:0}
  .brand{position:absolute;left:64px;top:72px;color:var(--orange);font-family:"Montserrat",sans-serif;font-weight:800;text-transform:uppercase}
  .brand-name{font-size:30px;line-height:32px;letter-spacing:.5px}
  .brand-site{font-size:15px;margin-top:6px;letter-spacing:.5px}
  .title{font-weight:400}
  .title-script{position:absolute;left:58px;top:238px;font-family:"Dancing Script",cursive;font-weight:700;font-size:88px;color:var(--orange);line-height:1}
  .title-main{position:absolute;left:56px;font-family:"Montserrat",sans-serif;font-weight:800;color:var(--teal);font-size:100px;line-height:1;letter-spacing:-2px}
  .title-plasma{top:350px}
  .title-therapy{top:444px}
  .title-acronym{position:absolute;left:568px;top:454px;writing-mode:vertical-rl;transform:rotate(180deg);font-family:"Outfit",sans-serif;font-size:23px;line-height:24px;color:var(--orange);letter-spacing:1px;font-weight:400}
  .intro{position:absolute;left:64px;top:574px;width:540px;font-size:15px;line-height:20px;font-weight:300}
  .intro p+p{margin-top:14px}
  .eligible{position:absolute;left:64px;top:694px;display:flex;align-items:center;gap:10px;padding:7px 16px;border:1.5px solid var(--teal);border-radius:20px;font-size:17px;font-weight:600;color:var(--teal);letter-spacing:.3px}
  .price{position:absolute;left:70px;top:788px}
  .price-label{font-size:30px;font-weight:400}
  .price-amount{font-family:"Montserrat",sans-serif;font-weight:800;color:var(--teal);font-size:92px;line-height:1;margin-top:4px;letter-spacing:-2px}
  .price-unit{font-size:29px;font-weight:400;margin-top:2px}
  .divider{position:absolute;left:359px;top:788px;height:168px;border-left:1.5px dashed var(--teal)}
  .treating{position:absolute;left:438px;top:776px}
  .treating-title{font-size:40px;font-weight:600;color:var(--orange);padding-bottom:8px;border-bottom:1px solid #6a6a6a;width:306px}
  .treating-list{list-style:none;margin-top:8px}
  .treating-list li{display:flex;align-items:center;gap:10px;font-size:22px;height:38px;padding-left:6px}
  .band{position:absolute;left:0;top:984px;width:934px;height:108px;background:var(--white);color:var(--dark-text);text-align:center}
  .band-services{font-family:"Outfit",sans-serif;font-weight:700;font-size:30px;margin-top:18px;letter-spacing:-.2px}
  .band-services .sep{color:var(--orange);font-weight:500;margin:0 18px}
  .band-note{font-size:26px;font-weight:400;margin-top:6px}
  .locations{position:absolute;left:0;top:1092px;width:934px;height:86px;background:linear-gradient(90deg,var(--teal),#a8a878 50%,var(--orange));display:flex}
  .location{position:relative;flex:1;display:flex;align-items:flex-start;padding:15px 0 0 36px;gap:12px;font-size:13.6px;line-height:17.5px;font-weight:300}
  .location+.location{border-left:1.5px dashed rgba(255,255,255,.8);margin:6px 0;padding-top:9px}
  .location strong{display:block;font-weight:600}
  .pin{flex:none;margin-top:2px}
  .footer-rule{position:absolute;left:0;top:1178px;width:934px;height:22px;background:var(--white)}
</style>
</head>
<body>
<main class="flyer">
  <svg class="hero-art" width="934" height="760" viewBox="0 0 934 760">
    <defs>
      <clipPath id="lab-clip"><circle cx="950" cy="50" r="452"/></clipPath>
      <linearGradient id="lab-tone" x1="0" y1="0" x2="1" y2="1">
        <stop offset="0" stop-color="#e9eef2"/>
        <stop offset=".55" stop-color="#9fb6c8"/>
        <stop offset="1" stop-color="#3f6e8c"/>
      </linearGradient>
      <radialGradient id="foot-tone" cx=".45" cy=".5" r=".6">
        <stop offset="0" stop-color="#b5533e"/>
        <stop offset=".5" stop-color="#6e4a3c"/>
        <stop offset="1" stop-color="#2f4454"/>
      </radialGradient>
    </defs>
    <circle cx="950" cy="50" r="460" fill="none" stroke="var(--orange)" stroke-width="8"/>
    <rect x="0" y="0" width="934" height="760" fill="url(#lab-tone)" clip-path="url(#lab-clip)" role="img" aria-label="Photo of a gloved hand holding a flask of blue liquid beside a laboratory microscope"/>
    <circle cx="757" cy="506" r="123" fill="var(--white)"/>
    <circle cx="757" cy="506" r="120" fill="url(#foot-tone)" role="img" aria-label="Photo of a person holding a sore heel, highlighted in red"/>
  </svg>

  <header class="brand">
    <div class="brand-name">Riverside<br>Foot &amp; Ankle</div>
    <div class="brand-site">stepwellclinic.com</div>
  </header>

  <h1 class="title">
    <span class="title-script">Platelet Rich</span>
    <span class="title-main title-plasma">PLASMA</span>
    <span class="title-main title-therapy">THERAPY</span>
    <span class="title-acronym">(PRP)</span>
  </h1>

  <section class="intro">
    <p>PRP uses the healing proteins in your own blood platelets to speed up tissue repair.</p>
    <p>Injected into damaged tissue, it helps your body grow new, healthy cells. A consultation is required.</p>
  </section>

  <div class="eligible">
    <svg width="18" height="18" viewBox="0 0 18 18"><circle cx="9" cy="9" r="7.5" fill="none" stroke="var(--teal)" stroke-width="1.8"/><path d="M5.5 9.2l2.4 2.4 4.8-5" fill="none" stroke="var(--teal)" stroke-width="1.8" stroke-linecap="round" stroke-linejoin="round"/></svg>
    FSA/HSA Eligible
  </div>

  <section class="price">
    <div class="price-label">Self Pay Price:</div>
    <div class="price-amount">$199</div>
    <div class="price-unit">Per Treatment</div>
  </section>

  <div class="divider"></div>

  <section class="treating">
    <h2 class="treating-title">Treating:</h2>
    <ul class="treating-list">
      <li><svg width="18" height="18" viewBox="0 0 18 18"><circle cx="9" cy="9" r="7.5" fill="none" stroke="var(--teal)" stroke-width="1.8"/><path d="M5.5 9.2l2.4 2.4 4.8-5" fill="none" stroke="var(--teal)" stroke-width="1.8" stroke-linecap="round" stroke-linejoin="round"/></svg>Plantar Fasciitis</li>
      <li><svg width="18" height="18" viewBox="0 0 18 18"><circle cx="9" cy="9" r="7.5" fill="none" stroke="var(--teal)" stroke-width="1.8"/><path d="M5.5 9.2l2.4 2.4 4.8-5" fill="none" stroke="var(--teal)" stroke-width="1.8" stroke-linecap="round" stroke-linejoin="round"/></svg>Tendon &amp; Ligament Injuries</li>
      <li><svg width="18" height="18" viewBox="0 0 18 18"><circle cx="9" cy="9" r="7.5" fill="none" stroke="var(--teal)" stroke-width="1.8"/><path d="M5.5 9.2l2.4 2.4 4.8-5" fill="none" stroke="var(--teal)" stroke-width="1.8" stroke-linecap="round" stroke-linejoin="round"/></svg>Achilles Tendonitis</li>
    </ul>
  </section>

  <section class="band">
    <div class="band-services">Same Day<span class="sep">|</span>Emergency<span class="sep">|</span>Saturday Appointments</div>
    <div class="band-note">Our Doctors are on call at the RMC ER 24/7</div>
  </section>

  <footer class="locations">
    <div class="location">
      <svg class="pin" width="24" height="30" viewBox="0 0 24 30"><path d="M12 0C5.4 0 0 5.2 0 11.6 0 20 12 30 12 30s12-10 12-18.4C24 5.2 18.6 0 12 0z" fill="var(--white)"/><circle cx="12" cy="11.5" r="4.5" fill="#5cbf9c"/></svg>
      <div><strong>Northgate Office</strong>210 Maple Grove Dr.<br>Ste. 140 Ashford, MD 21090</div>
    </div>
    <div class="location">
      <svg class="pin" width="24" height="30" viewBox="0 0 24 30"><path d="M12 0C5.4 0 0 5.2 0 11.6 0 20 12 30 12 30s12-10 12-18.4C24 5.2 18.6 0 12 0z" fill="var(--white)"/><circle cx="12" cy="11.5" r="4.5" fill="#a8a878"/></svg>
      <div><strong>Hillcrest Office</strong>88 Wellness Way<br>Hillcrest, WV 25490</div>
    </div>
    <div class="location">
      <svg class="pin" width="24" height="30" viewBox="0 0 24 30"><path d="M12 0C5.4 0 0 5.2 0 11.6 0 20 12 30 12 30s12-10 12-18.4C24 5.2 18.6 0 12 0z" fill="var(--white)"/><circle cx="12" cy="11.5" r="4.5" fill="#ec7f48"/></svg>
      <div><strong>Lakeview Office</strong>5120 Orchard Park Blvd. Ste. 300<br>Lakeview, MD 21780</div>
    </div>
  </footer>
  <div class="footer-rule"></div>
</main>
</body>
</html>
```